Need a flyer overhaul and minor changes

flyer is 5.5" x 8.5" we need to change the $250.00 to $325.00, update our company logo on the brochure, and also have an area where we can have the store address (318 W Harlan Ave, Del Rio, TX 78840 - (830) 642-9158). I've attached a our current brochure and our updated logo and we just want to make look better and updated.

Industry/Entity Type

Lending and Finance

Requirements
Nice to have
• updated layout and pictures

```html
<!DOCTYPE html>
<html lang="en">
<head>
<meta charset="utf-8">
<title>Stuck in a Title Loan? – Crestline Finance</title>
<link rel="stylesheet" href="https://fonts.googleapis.com/css2?family=Montserrat:wght@400;500;600;700;800&family=Oswald:wght@600&display=swap">
<style>
  :root {
    --brand-red: #c1252a;
    --brand-green: #245535;
    --ink-green: #1f4a2e;
    --row-green: #3d8c58;
    --paper: #ffffff;
    --stage: #e4e4e4;
    --sun-light: #fff7cf;
    --sun-deep: #fde35e;
    --shirt: #cfe0ee;
  }
  * { box-sizing: border-box; margin: 0; padding: 0; }
  html, body { width: 857px; height: 1200px; overflow: hidden; }
  body { background: var(--stage); font-family: "Montserrat", Arial, sans-serif; }

  .flyer { position: absolute; left: 40px; top: 0; width: 776px; height: 1200px; background: var(--paper); overflow: hidden; }

  .headline-band { position: absolute; left: 0; top: 0; width: 776px; height: 151px; background: var(--brand-red);
    display: flex; align-items: center; justify-content: center; color: var(--paper); font-size: 53px; font-weight: 500; letter-spacing: -0.5px; }
  .headline-band strong { font-weight: 800; margin-left: 14px; }

  .hero-photo { position: absolute; left: 0; top: 151px; width: 282px; height: 798px;
    background: linear-gradient(180deg, var(--sun-light) 0%, var(--sun-deep) 55%, var(--shirt) 72%, #e9f1f7 100%); }

  .comparison-panel { position: absolute; left: 282px; top: 151px; width: 494px; height: 798px; background: var(--brand-green); }
  .comparison-title { position: absolute; right: 52px; top: 22px; color: var(--paper); font-size: 25px; font-weight: 800; }

  .comparison-table { position: absolute; left: 18px; top: 69px; width: 476px; height: 668px; background: var(--paper); }
  .col-brand { position: absolute; left: 43px; top: 40px; width: 150px; color: var(--ink-green); font-weight: 700; font-size: 18px; line-height: 1.1; text-align: center; }
  .col-brand small { display: block; font-size: 8px; letter-spacing: 2px; margin-top: 3px; }
  .col-title { position: absolute; right: 51px; top: 42px; color: var(--ink-green); font-family: "Oswald", "Arial Narrow", sans-serif; font-size: 40px; font-weight: 600; line-height: 1; }
  .rule-top, .rule-bottom { position: absolute; left: 43px; width: 380px; height: 2px; background: var(--ink-green); }
  .rule-top { top: 109px; }
  .rule-bottom { top: 533px; }
  .rule-mid { position: absolute; left: 233px; top: 109px; width: 2px; height: 425px; background: var(--ink-green); }

  .payments { position: absolute; top: 130px; list-style: none; font-size: 20px; font-weight: 600; }
  .payments li { height: 32px; line-height: 32px; display: flex; }
  .payments .num { width: 34px; text-align: center; color: var(--row-green); font-weight: 500; margin-right: 14px; }
  .payments .amt { color: var(--ink-green); }
  .payments.ours { left: 48px; }
  .payments.theirs { left: 264px; }

  .result-paid { position: absolute; left: 43px; top: 553px; color: var(--ink-green); font-size: 29px; font-weight: 800; }
  .result-owe { position: absolute; right: 53px; top: 553px; color: var(--brand-red); font-size: 29px; font-weight: 800; }
  .owe-amount { position: absolute; right: 53px; top: 590px; width: 172px; height: 53px; background: var(--brand-red);
    color: var(--paper); font-size: 42px; font-weight: 800; display: flex; align-items: center; justify-content: center; }

  .spanish-band { position: absolute; right: 52px; top: 754px; color: var(--paper); font-size: 29px; font-weight: 800; }

  .store-info { position: absolute; left: 0; top: 949px; width: 776px; height: 167px; background: var(--paper); }
  .store-brand { position: absolute; left: 51px; top: 48px; width: 224px; color: var(--ink-green); font-weight: 700; font-size: 34px; line-height: 1.05; text-align: center; }
  .store-brand small { display: block; font-size: 11px; letter-spacing: 3px; margin-top: 6px; }
  .store-phone { position: absolute; right: 51px; top: 36px; color: var(--brand-red); font-size: 50px; font-weight: 800; letter-spacing: -1px; }
  .store-address { position: absolute; right: 51px; top: 108px; color: var(--ink-green); font-size: 20px; font-weight: 600; }

  .web-band { position: absolute; left: 0; top: 1116px; width: 776px; height: 84px; background: var(--brand-red);
    display: flex; align-items: center; justify-content: center; color: var(--paper); font-size: 24px; letter-spacing: 5px; }
  .web-band .visit { font-weight: 400; margin-right: 14px; }
  .web-band .url { font-weight: 800; letter-spacing: 4px; }
</style>
</head>
<body>
<main class="flyer">
  <header class="headline-band">Stuck in a <strong>Title Loan?</strong></header>

  <div class="hero-photo" role="img" aria-label="Photo of a smiling woman in a light blue shirt counting a stack of cash against a warm yellow background"></div>

  <section class="comparison-panel">
    <h2 class="comparison-title">$1,000 LOAN COMPARISON</h2>
    <div class="comparison-table">
      <div class="col-brand">Crestline Finance<small>FINANCE</small></div>
      <div class="col-title">TITLE LOAN</div>
      <div class="rule-top"></div>
      <div class="rule-mid"></div>
      <ol class="payments ours">
        <li><span class="num">1</span><span class="amt">$131.67</span></li>
        <li><span class="num">2</span><span class="amt">$131.67</span></li>
        <li><span class="num">3</span><span class="amt">$131.67</span></li>
        <li><span class="num">4</span><span class="amt">$131.67</span></li>
        <li><span class="num">5</span><span class="amt">$131.67</span></li>
        <li><span class="num">6</span><span class="amt">$131.67</span></li>
        <li><span class="num">7</span><span class="amt">$131.67</span></li>
        <li><span class="num">8</span><span class="amt">$131.67</span></li>
        <li><span class="num">9</span><span class="amt">$131.67</span></li>
        <li><span class="num">10</span><span class="amt">$131.67</span></li>
        <li><span class="num">11</span><span class="amt">$131.67</span></li>
        <li><span class="num">12</span><span class="amt">$131.67</span></li>
      </ol>
      <ol class="payments theirs">
        <li><span class="num">1</span><span class="amt">$325.00</span></li>
        <li><span class="num">2</span><span class="amt">$325.00</span></li>
        <li><span class="num">3</span><span class="amt">$325.00</span></li>
        <li><span class="num">4</span><span class="amt">$325.00</span></li>
        <li><span class="num">5</span><span class="amt">$325.00</span></li>
        <li><span class="num">6</span><span class="amt">$325.00</span></li>
        <li><span class="num">7</span><span class="amt">$325.00</span></li>
        <li><span class="num">8</span><span class="amt">$325.00</span></li>
        <li><span class="num">9</span><span class="amt">$325.00</span></li>
        <li><span class="num">10</span><span class="amt">$325.00</span></li>
        <li><span class="num">11</span><span class="amt">$325.00</span></li>
        <li><span class="num">12</span><span class="amt">$325.00</span></li>
      </ol>
      <div class="rule-bottom"></div>
      <div class="result-paid">PAID OFF</div>
      <div class="result-owe">STILL OWE</div>
      <div class="owe-amount">$1,000</div>
    </div>
    <div class="spanish-band">SE HABLA ESPAÑOL</div>
  </section>

  <section class="store-info">
    <div class="store-brand">Crestline Finance<small>FINANCE</small></div>
    <div class="store-phone">(830) 642-9158</div>
    <div class="store-address">318 W Harlan Ave, Del Rio, TX 78840</div>
  </section>

  <footer class="web-band"><span class="visit">VISIT US AT</span><span class="url">CRESTLINEFINANCE.COM</span></footer>
</main>
</body>
</html>
```